The Hidden Storm Beneath Your Garden Book Cover

Need a book cover that jumps out, simple is good. I am trying to relay to readers that they face a serious tax burden when they reach retirement.

I am attaching the cover I've been using, which I designed, but it's not nearly effective enough.
Get rid of the word "Accounts" in the cover, please.

```html
<!DOCTYPE html>
<html lang="en">
<head>
<meta charset="utf-8">
<title>The Hidden Storm Beneath Your Garden — Book Cover</title>
<link rel="stylesheet" href="https://fonts.googleapis.com/css2?family=Cinzel:wght@400;600;700&display=swap">
<style>
  :root {
    --backdrop: #262626;
    --paper: #ffffff;
    --title-ink: #1b2a1c;
    --accent-green: #1f6b35;
    --cash-tan: #d9c09a;
    --cash-green: #b9c2a4;
    --stick-tan: #e3cfa7;
  }
  * { margin: 0; padding: 0; box-sizing: border-box; }
  html, body {
    width: 1200px;
    height: 905px;
    overflow: hidden;
    background: var(--backdrop);
  }
  .stage {
    width: 1200px;
    height: 905px;
    display: flex;
    align-items: center;
    justify-content: center;
  }
  .book-cover {
    width: 580px;
    height: 865px;
    background: var(--paper);
    display: flex;
    flex-direction: column;
    align-items: center;
    padding-top: 88px;
    font-family: "Cinzel", "Trajan Pro", serif;
  }
  .book-title {
    color: var(--title-ink);
    font-weight: 700;
    font-size: 46px;
    line-height: 1.34;
    text-align: center;
    letter-spacing: -0.5px;
  }
  .book-title span { display: block; }
  .book-subtitle {
    margin-top: 16px;
    color: var(--accent-green);
    font-weight: 400;
    font-size: 20px;
    line-height: 1.4;
    text-align: center;
    letter-spacing: 1px;
  }
  .cover-art {
    margin-top: 36px;
    width: 470px;
    height: 340px;
  }
  .author-name {
    margin-top: auto;
    margin-bottom: 78px;
    color: var(--accent-green);
    font-size: 26px;
    font-weight: 400;
    letter-spacing: 17px;
    text-align: center;
  }
</style>
</head>
<body>
<main class="stage">
  <article class="book-cover">
    <h1 class="book-title">
      <span>The Hidden Storm</span>
      <span>Beneath Your</span>
      <span>Garden</span>
    </h1>
    <p class="book-subtitle">And how the Roth IRA<br>can help you avoid it</p>
    <svg class="cover-art" viewBox="0 0 470 340" role="img" aria-label="Illustration: bundle of dynamite with a digital timer resting on stacks of banded hundred-dollar bills">
      <defs>
        <radialGradient id="artTone" cx="50%" cy="50%" r="55%">
          <stop offset="0%" stop-color="var(--stick-tan)"/>
          <stop offset="60%" stop-color="var(--cash-tan)"/>
          <stop offset="100%" stop-color="var(--cash-green)" stop-opacity="0"/>
        </radialGradient>
      </defs>
      <ellipse cx="235" cy="170" rx="235" ry="170" fill="url(#artTone)"/>
    </svg>
    <p class="author-name">Reid Calloway</p>
  </article>
</main>
</body>
</html>
```